custom carpentry, woodworking and home repair company needs logo design and business card design

Attention: I apologize but I just received notification from my state that I cannot use the company name that I originally submitted (Beyond The Bench). The new name will be Lumbrella We need a company logo and business card design for our new company based in the Hampton Roads area of Virginia. The company name is Lumbrella. The final design should give a first impression of true craftsmanship and attention to detail. We would like the card to include the company name, my name Derek Halloway (owner), phone number (757) 482-3175, website (lumbrella-shop.example) and email address (derek@lumbrella-shop.example). Everything else is up to your discretion. Thanks, have fun, and good luck.

Industry/Entity Type

Business

Contact Information for Business Card

See project description

Logo Text

see project description

Colors

Designer to choose colors to be used in the design.

```html
<!DOCTYPE html>
<html lang="en">
<head>
<meta charset="utf-8">
<title>Lumbrella — Business Card</title>
<link rel="stylesheet" href="https://fonts.googleapis.com/css2?family=Montserrat:wght@600;700&family=Lato:wght@400&display=swap">
<style>
  :root {
    --stage: #1b1b1b;
    --card-light: #f2f2f2;
    --amber: #d38b1f;
    --ink: #141414;
    --rule: #222222;
  }
  * { margin: 0; padding: 0; box-sizing: border-box; }
  html, body { width: 1200px; height: 900px; overflow: hidden; background: var(--stage); }
  .stage { position: relative; width: 1200px; height: 900px; }
  .card { position: absolute; top: 170px; width: 347px; height: 561px; }
  .card--front { left: 259px; background: var(--card-light); }
  .card--back { left: 631px; background: var(--amber); }

  .wordmark {
    position: absolute; left: 0; right: 0; text-align: center;
    font-family: "Montserrat", sans-serif; font-weight: 700;
    font-size: 38px; letter-spacing: 2.5px; color: var(--ink); line-height: 1;
  }
  .card--front .wordmark { top: 151px; }
  .card--back .wordmark { top: 262px; }

  .holder { position: absolute; top: 326px; left: 0; right: 0; text-align: center; }
  .holder__name {
    font-family: "Montserrat", sans-serif; font-weight: 600;
    font-size: 23px; color: var(--amber); letter-spacing: 0.3px; line-height: 1;
  }
  .holder__role {
    margin-top: 4px;
    font-family: "Lato", sans-serif; font-size: 15px; color: var(--ink);
  }
  .divider {
    position: absolute; top: 391px; left: 101px; width: 145px; height: 1px; background: var(--rule);
  }
  .contact-icons {
    position: absolute; top: 412px; left: 0; right: 0;
    display: flex; justify-content: center; gap: 6px;
  }
  .contact-icons svg { width: 11px; height: 11px; fill: var(--amber); }
  .contact {
    position: absolute; top: 430px; left: 0; right: 0; text-align: center;
    font-family: "Lato", sans-serif; font-size: 15px; color: var(--ink); line-height: 20.5px;
  }
  .contact__region { margin-top: 10px; }
</style>
</head>
<body>
<main class="stage">
  <section class="card card--front">
    <div class="wordmark">LUMBRELLA</div>
    <div class="holder">
      <p class="holder__name">DEREK HALLOWAY</p>
      <p class="holder__role">Owner</p>
    </div>
    <div class="divider"></div>
    <div class="contact-icons" aria-hidden="true">
      <svg viewBox="0 0 12 12"><path d="M2.5 0.8l2 2-1 1.4c.6 1.5 1.8 2.7 3.3 3.3l1.4-1 2 2-1.3 1.8C4.8 10 1.9 7.2 0.8 2.1z"/></svg>
      <svg viewBox="0 0 12 12"><path d="M0.5 2.5h11L6 6.3z M0.5 3.6v6h11v-6L6 7.6z"/></svg>
      <svg viewBox="0 0 12 12"><circle cx="6" cy="6" r="5.4"/><path d="M4 3.2c1 .4 1.2 1.3.6 2-.7.6-.2 1.6.6 1.7.8.1.8 1.3.3 2.2" fill="none" stroke="#f2f2f2" stroke-width="1"/></svg>
    </div>
    <div class="contact">
      <p class="contact__phone">(757) 482-3175</p>
      <p class="contact__email">derek@lumbrella-shop.example</p>
      <p class="contact__web">www.lumbrella-shop.example</p>
      <p class="contact__region">Harlow Point, Maryland</p>
    </div>
  </section>

  <section class="card card--back">
    <div class="wordmark">LUMBRELLA</div>
  </section>
</main>
</body>
</html>
```